yourSmileCare Brookvale Business Card

Please design a two sided business card that is Elegant and Professional
Add subtle elegant patterns to suit Spot UV printing/ or raised printing

Name: Dr Marcus T. Fenwick
Qualification: BDSc (QLD)
Title: Dental Surgeon, Clinical Director
Company: yourSmileCare Brookvale
Phone: (02) 7593 2268
Address: Shop 7/18-20 Lindon Ave Brookvale 2097
email: info@yoursmilecarebrookvale.com.au
Facebook: facebook.com/yoursmilecarebrookvale

Motto:
Quality dentistry you can trust

Description of services (not compulsory):
Preventative Dentistry | General Dentistry
Cosmetic Dentistry | Teeth Whitening
Crown and Bridge | Root Canal Therapy
Veneers | Clearvono | Orthodontics
Emergency Dental Care | After Hours

Personalised Treatment Plans
Transparent Fees

Please make sure card is elegant and professional

Target Market(s)

general population, patients,
Dental sales companies, other professions

Industry/Entity Type

Dental Clinic

Contact Information for Business Card

Name: Dr Marcus T. Fenwick
Qualification: BDSc (QLD)
Phone: (02) 7593 2268
Address: Shop 7/18-20 Lindon Ave Brookvale

Motto:

Description of services (not compulsory)

Transparent Fees

Image of dental surgery optional

Please make sure card is elegant and profession

Requirements
Must have
• Logo
• Name, Title (next to name), Business
• Phone, address, facbeook
• Must have stylish design to suit SPOT UV reflective printing
Nice to have
• Subtle elegant patterns which will have Spot UV on them when printed
• Colours to match logo colour
• Description of services
Should not have
• Small fonts that are hard to read
• DO NOT PUT IMAGES OF DENTAL INSTRUMENTS OR TEETH PLEASE

```html
<!DOCTYPE html>
<html lang="en">
<head>
<meta charset="utf-8">
<title>yourSmileCare Brookvale – Business Card</title>
<link rel="stylesheet" href="https://fonts.googleapis.com/css2?family=Lato:ital,wght@0,400;0,700;0,900;1,700&display=swap">
<style>
  :root {
    --stage: #262626;
    --green: #8cc63f;
    --green-light: #a3d65a;
    --green-dark: #74ad2c;
    --grey: #6a6a6a;
    --grey-dark: #4a4a4a;
    --ink: #222222;
    --paper: #ffffff;
    --paper-shade: #eeeeee;
    --divider: #e2e2e2;
  }
  * { box-sizing: border-box; margin: 0; padding: 0; }
  html, body {
    width: 1200px; height: 873px; overflow: hidden;
    background: var(--stage);
    font-family: "Lato", Arial, sans-serif;
  }
  .sheet {
    width: 1200px; height: 873px;
    display: flex; align-items: center; justify-content: center; gap: 40px;
  }
  .card {
    position: relative;
    width: 560px; height: 342px;
    border-radius: 20px;
    overflow: hidden;
  }

  /* Back side */
  .card--back {
    background: linear-gradient(135deg, var(--green-light), var(--green) 55%, var(--green-dark));
    color: var(--paper);
  }
  .services {
    position: absolute; right: 34px; top: 110px;
    text-align: right;
    font-size: 13.5px; font-weight: 700; line-height: 1.75;
  }
  .services .sep { opacity: 0.7; margin: 0 4px; font-weight: 400; }
  .motto {
    position: absolute; right: 34px; bottom: 42px;
    font-size: 12px; font-weight: 700;
    letter-spacing: 0.32em; text-transform: uppercase;
  }

  /* Front side */
  .card--front {
    background: linear-gradient(160deg, var(--paper), var(--paper-shade));
    color: var(--grey);
  }
  .card--front .fold-line {
    position: absolute; left: 50%; top: 0; bottom: 0;
    width: 1px; background: var(--divider);
  }
  .holder { position: absolute; left: 44px; top: 56px; }
  .holder__name {
    font-size: 20px; font-weight: 900; color: var(--grey);
    white-space: nowrap;
  }
  .holder__qual { font-size: 11px; font-weight: 400; margin-left: 6px; }
  .holder__title {
    font-size: 14px; font-weight: 700; font-style: italic;
    color: var(--ink); margin-top: 2px;
  }
  .brand {
    position: absolute; right: 34px; top: 70px;
    display: flex; align-items: center; gap: 10px;
  }
  .brand__dot {
    width: 22px; height: 22px; border-radius: 50%; background: var(--green);
  }
  .brand__name {
    font-size: 23px; font-weight: 900; color: var(--grey-dark);
    line-height: 1.05; text-align: right;
  }
  .contact-tab {
    position: absolute; left: 0; top: 168px;
    width: 48px; height: 174px;
    background: var(--green);
    border-radius: 0 16px 0 0;
    display: flex; flex-direction: column; align-items: center;
    justify-content: space-around; padding: 12px 0 16px;
  }
  .contact-tab svg { width: 18px; height: 18px; fill: var(--paper); }
  .contact-list {
    position: absolute; left: 66px; top: 184px;
    list-style: none;
    font-size: 15px; font-weight: 700; color: var(--grey);
    line-height: 36.5px;
    white-space: nowrap;
  }
</style>
</head>
<body>
<main class="sheet">

  <section class="card card--back" aria-label="Business card back">
    <p class="services">
      Preventative Dentistry<span class="sep">|</span>General Dentistry<span class="sep">|</span>Cosmetic Dentistry<br>
      Teeth Whitening<span class="sep">|</span>Crown and Bridge<span class="sep">|</span>Root Canal Therapy<span class="sep">|</span>Veneers<br>
      Clearvono<span class="sep">|</span>Orthodontics<span class="sep">|</span>Emergency Dental Care<span class="sep">|</span>After Hours<br>
      Personalised Treatment Plans<span class="sep">|</span>Transparent Fees
    </p>
    <p class="motto">Quality dentistry you can trust</p>
  </section>

  <section class="card card--front" aria-label="Business card front">
    <div class="fold-line"></div>

    <div class="holder">
      <p class="holder__name">Dr Marcus T. Fenwick<span class="holder__qual">BDSc (QLD)</span></p>
      <p class="holder__title">Dental Surgeon, Clinical Director</p>
    </div>

    <div class="brand">
      <span class="brand__dot"></span>
      <span class="brand__name">yourSmileCare<br>Brookvale</span>
    </div>

    <div class="contact-tab">
      <svg viewBox="0 0 24 24" role="img" aria-label="Phone"><path d="M6.6 10.8a15.1 15.1 0 0 0 6.6 6.6l2.2-2.2c.3-.3.7-.4 1-.2 1.1.4 2.3.6 3.6.6.6 0 1 .4 1 1V20c0 .6-.4 1-1 1A17 17 0 0 1 3 4c0-.6.4-1 1-1h3.5c.6 0 1 .4 1 1 0 1.3.2 2.5.6 3.6.1.3 0 .7-.2 1z"/></svg>
      <svg viewBox="0 0 24 24" role="img" aria-label="Social page"><circle cx="12" cy="12" r="8"/></svg>
      <svg viewBox="0 0 24 24" role="img" aria-label="Email"><path d="M3 5h18v14H3z" fill="none" stroke="#fff" stroke-width="2"/><path d="M3 5l9 8 9-8" fill="none" stroke="#fff" stroke-width="2"/></svg>
      <svg viewBox="0 0 24 24" role="img" aria-label="Address"><path d="M12 2a7 7 0 0 0-7 7c0 5.2 7 13 7 13s7-7.8 7-13a7 7 0 0 0-7-7zm0 9.5A2.5 2.5 0 1 1 12 6.5a2.5 2.5 0 0 1 0 5z"/></svg>
    </div>

    <ul class="contact-list">
      <li>(02) 7593 2268</li>
      <li>/yoursmilecarebrookvale</li>
      <li>info@yoursmilecarebrookvale.com.au</li>
      <li>Shop 7/18-20 Lindon Ave Brookvale 2097</li>
    </ul>
  </section>

</main>
</body>
</html>
```